Stationary and Business Card Design

We need a stationery design and a business card design for a non-profit economics development agency. Our website is brightledgerhub.org. Our clients are Canadian government agencies and large Chinese company. We need the design to be professional and corporate.

Please see attached for our Power Point presentation. Please take design elements from our website and our ppt.

```html
<!DOCTYPE html>
<html lang="en">
<head>
<meta charset="utf-8">
<title>Bright Ledger Alliance — Letterhead</title>
<link rel="stylesheet" href="https://fonts.googleapis.com/css2?family=Tinos:wght@400;700&family=Arimo:wght@400&display=swap">
<style>
  :root{
    --bg:#e9e9e9;
    --paper:#fbfbfb;
    --ink:#1b1b1b;
    --brand:#e0171f;
    --muted:#444;
  }
  *{box-sizing:border-box;margin:0;padding:0}
  html,body{width:1200px;height:795px;overflow:hidden;background:var(--bg)}
  .letterhead{
    position:absolute;left:330px;top:16px;width:540px;height:763px;
    background:var(--paper);box-shadow:0 2px 10px rgba(0,0,0,.12);
    font-family:"Tinos","Times New Roman",serif;color:var(--ink);
  }
  .brand{
    position:absolute;left:62px;top:62px;display:flex;align-items:center;gap:7px;
  }
  .brand-mark{width:14px;height:14px;background:var(--brand)}
  .brand-name{font-family:"Tinos",serif;font-weight:700;font-size:13px;color:var(--brand)}
  .letter-body{
    position:absolute;left:62px;top:128px;width:418px;
    font-size:9.4px;line-height:1.32;text-align:justify;
  }
  .letter-body p{margin-bottom:11px}
  .sign-off{
    position:absolute;left:232px;top:420px;font-size:9.4px;font-weight:700;line-height:1.3;
  }
  .signature{display:block;width:90px;height:30px;margin:6px 0 3px;background:linear-gradient(90deg,#d8d8d8,#e8e8e8);border-radius:3px}
  .contact{
    position:absolute;left:395px;top:662px;list-style:none;
    font-family:"Arimo",Arial,sans-serif;font-size:7.4px;color:var(--muted);
  }
  .contact li{display:flex;align-items:center;gap:8px;height:12.5px}
  .contact svg{width:8px;height:8px;flex:none}
</style>
</head>
<body>
<main class="letterhead">
  <div class="brand">
    <span class="brand-mark"></span>
    <span class="brand-name">Bright Ledger Alliance</span>
  </div>

  <section class="letter-body">
    <p>Gentlemen,</p>
    <p>Enclosed I have the honor to send you an article which I should be pleased if you would accept for the “Civic Quarterly Review”. I am desperately pushed for money; and in the event of Mr. Halloran’s liking the “Landscape-Garden”, I would take it as an especial favor if you would mail me the amount due for it, so as to reach me here by the 21st, on which day I shall need it. Can you possibly oblige me in this? If you accept the paper I presume you will allow me your usual sum, whatever that is, for similar contributions—but I set no price—leaving all to your own liberality. The piece will make 8 of your pages and rather more.</p>
    <p>Will you be kind enough to put the best possible interpretation upon my behavior while in N-York? You must have conceived a queer idea of me—but the simple truth is that Whitcombe would insist upon the <em>juleps</em>, and I knew not what I was either doing or saying. The Review of Darby which I offered you was deficient in a ½ page of commencement, which I had written to supersede the old beginning, and which gave the article the character of a general and retrospective review. No wonder you did not take it—I would have been very much mortified if you had. I hope to see you at some future time, under better auspices.</p>
  </section>

  <div class="sign-off">
    In the meantime I remain<br>Yours very truly,
    <span class="signature" role="img" aria-label="Handwritten signature"></span>
    Edwin Harlow Price
  </div>

  <ul class="contact">
    <li><svg viewBox="0 0 8 8"><rect width="8" height="8" fill="#e0171f"/><path d="M2 1.6h1.2l.5 1.4-.8.6a3.5 3.5 0 0 0 1.5 1.5l.6-.8 1.4.5V6A.9.9 0 0 1 5.5 6.8 4.6 4.6 0 0 1 1.2 2.5 .9.9 0 0 1 2 1.6z" fill="#fff"/></svg>+49 (0) 40 55501234</li>
    <li><svg viewBox="0 0 8 8"><rect width="8" height="8" fill="#e0171f"/><rect x="2.6" y="1.3" width="2.8" height="5.4" rx=".5" fill="#fff"/></svg>+49 (0) 151 55509876</li>
    <li><svg viewBox="0 0 8 8"><rect width="8" height="8" fill="#e0171f"/><rect x="1.4" y="2.2" width="5.2" height="3.6" fill="#fff"/><path d="M1.4 2.2 4 4.3l2.6-2.1" fill="none" stroke="#e0171f" stroke-width=".6"/></svg>jhon@brightledgerhub.org</li>
    <li><svg viewBox="0 0 8 8"><rect width="8" height="8" fill="#e0171f"/><circle cx="4" cy="4" r="2.5" fill="none" stroke="#fff" stroke-width=".7"/><path d="M1.5 4h5M4 1.5v5" stroke="#fff" stroke-width=".5"/></svg>www.brightledgerhub.org</li>
  </ul>
</main>
</body>
</html>
```